Residential home builder needs a fresh looking business card

We require a fresh looking business card for our business. We like the clean modern look. I have uploaded out logo and our email footer that incorporates some different elements. Blacks and Whites are good but i will leave this up to the design crowd creative minds.

our slogan is:
your idea of the perfect home

website (temporary site) but similar look and feel to the finished one
pinegrovedwellings.com.au

We also have intentions to apply the same look and feel to the rest of our stationary (letterheads, envelopes, site signs, vehicles etc)

Home Builder

```html
<!DOCTYPE html>
<html lang="en">
<head>
<meta charset="utf-8">
<title>Pinegrove Dwellings – Business Card</title>
<link rel="stylesheet" href="https://fonts.googleapis.com/css2?family=Open+Sans:wght@400;600;700&display=swap">
<style>
  :root {
    --brand-yellow: #f7dc1f;
    --brand-gold: #f0c419;
    --ink: #1e1e1e;
    --text-grey: #4a4a4a;
    --card-white: #ffffff;
    --backdrop: #e9e9e6;
  }
  * { box-sizing: border-box; margin: 0; padding: 0; }
  html, body { width: 1200px; height: 675px; overflow: hidden; }
  body {
    background: var(--backdrop);
    font-family: "Open Sans", Arial, sans-serif;
    display: flex;
    align-items: center;
    justify-content: center;
    gap: 56px;
  }
  .card {
    position: relative;
    width: 525px;
    height: 300px;
    border-radius: 4px;
    overflow: hidden;
    box-shadow: 0 6px 20px rgba(0,0,0,0.12);
  }
  .card-front { background: var(--card-white); }
  .card-back {
    background: var(--brand-yellow);
    display: flex;
    align-items: center;
    justify-content: center;
  }

  .wordmark {
    display: flex;
    align-items: center;
    gap: 10px;
    font-family: "Open Sans", Arial, sans-serif;
    font-weight: 600;
    color: var(--ink);
    letter-spacing: 0.04em;
    white-space: nowrap;
  }
  .wordmark-square {
    width: 14px; height: 14px;
    background: var(--brand-gold);
  }
  .card-front .wordmark {
    position: absolute;
    left: 34px; top: 58px;
    font-size: 24px;
  }
  .card-back .wordmark { font-size: 30px; }
  .card-back .wordmark-square { background: var(--ink); width: 18px; height: 18px; }

  .brand-decoration {
    position: absolute;
    right: 0; top: 0;
    width: 190px; height: 300px;
    background: linear-gradient(160deg, var(--brand-gold) 0%, var(--brand-gold) 55%, #2b2b2b 55%, #2b2b2b 100%);
  }

  .contact {
    position: absolute;
    left: 34px; top: 128px;
    color: var(--text-grey);
    font-size: 12px;
    line-height: 1.4;
  }
  .contact-name {
    color: var(--brand-gold);
    font-weight: 700;
    font-size: 17px;
    line-height: 1.2;
  }
  .contact-title { margin-bottom: 14px; }
  .contact-address { margin-bottom: 4px; }
  .contact-line {
    display: flex;
    align-items: center;
    gap: 8px;
  }
  .contact-line svg { width: 12px; height: 12px; flex: none; }
</style>
</head>
<body>

  <section class="card card-front">
    <div class="wordmark"><span class="wordmark-square"></span>Pinegrove Dwellings</div>

    <div class="contact">
      <p class="contact-name">Mark Ellison</p>
      <p class="contact-title">President CEO</p>
      <p class="contact-address">1480 Harbour Ridge Rd,<br>Ste 210 Fairview,<br>Texas 77512 USA</p>
      <p class="contact-line">
        <svg viewBox="0 0 12 12" aria-hidden="true"><path d="M1 4.5c0-1.4 1.2-2.5 5-2.5s5 1.1 5 2.5v1H8.5V4.2h-5v1.3H1z M3 6h6l1 4.5H2z" fill="#f0c419"/></svg>
        +1 (555) 318-4720
      </p>
      <p class="contact-line">
        <svg viewBox="0 0 12 12" aria-hidden="true"><circle cx="6" cy="6" r="5" fill="none" stroke="#f0c419" stroke-width="1.4"/><path d="M1 6h10M6 1c-2.5 3-2.5 7 0 10M6 1c2.5 3 2.5 7 0 10" fill="none" stroke="#f0c419" stroke-width="1"/></svg>
        www.pinegrovedwellings.com.au
      </p>
    </div>

    <div class="brand-decoration" role="img" aria-label="Large brand mark decoration in gold and charcoal"></div>
  </section>

  <section class="card card-back">
    <div class="wordmark"><span class="wordmark-square"></span>Pinegrove Dwellings</div>
  </section>

</body>
</html>
```